Billboard design for property management

DEADLINE 3RD APRIL 2022
I need a billboard design sized 390cm x 275 cm with 10cm bleed.

It needs to attract potential homeowners who want to make money by renting out their property to holidays

White background with orange and grey (as in the logo) maybe with an image. It must somehow, incorporate the boost your bookings attached.

Needs to show web address and phone number

```html
<!DOCTYPE html>
<html lang="en">
<head>
<meta charset="utf-8">
<title>Harbourline Property Management – Holiday Rentals Billboard</title>
<link href="https://fonts.googleapis.com/css2?family=Montserrat:wght@600;800;900&display=swap" rel="stylesheet">
<style>
  :root {
    --orange: #e8720c;
    --grey: #58595b;
    --grey-band: #6b6c6e;
    --white: #ffffff;
    --stage: #8c8c8c;
    --photo-light: #d9dde3;
    --photo-dark: #5b6f8c;
    --pattern-a: #f7e3cf;
    --pattern-b: #e6e6e6;
  }
  * { box-sizing: border-box; margin: 0; padding: 0; }
  html, body {
    width: 812px; height: 1200px; overflow: hidden;
    background: var(--stage);
    font-family: "Montserrat", Arial, sans-serif;
  }
  .billboard {
    position: absolute; left: 26px; top: 333px;
    width: 760px; height: 534px;
    background: var(--white);
    overflow: hidden;
  }
  .billboard__shapes { position: absolute; inset: 0; }
  .pattern-area {
    position: absolute; left: 470px; top: 0; width: 290px; height: 300px;
    background: linear-gradient(135deg, var(--pattern-b), var(--pattern-a) 55%, rgba(255,255,255,0));
    clip-path: polygon(20% 0, 100% 0, 100% 100%, 0 30%);
  }
  .model-photo {
    position: absolute; inset: 0;
    background: linear-gradient(180deg, var(--photo-light) 0%, #b7c1cf 45%, var(--photo-dark) 100%);
    clip-path: polygon(590px 62px, 760px 62px, 760px 534px, 372px 534px, 380px 410px, 430px 335px, 520px 300px, 560px 250px, 572px 160px);
  }
  .headline { position: absolute; left: 38px; top: 58px; font-weight: 800; text-transform: uppercase; line-height: 1; }
  .headline__lead { color: var(--orange); font-size: 51px; letter-spacing: 0.5px; }
  .headline__main { color: var(--grey); font-size: 51px; margin-top: 6px; letter-spacing: 0.3px; }
  .headline__sub { color: var(--grey); font-size: 26px; margin-top: 12px; }
  .headline__sub--indent { margin-left: 64px; margin-top: 6px; }
  .headline__mark {
    position: absolute; left: 356px; top: 150px;
    color: var(--orange); font-size: 90px; font-weight: 900; line-height: 1;
  }
  .campaign {
    position: absolute; left: 38px; top: 322px; color: var(--white);
    font-weight: 900; text-transform: uppercase; font-size: 19px; line-height: 1.02;
  }
  .campaign__with {
    position: absolute; left: 148px; top: 318px; color: var(--white);
    font-size: 11px; font-weight: 800; letter-spacing: 1px;
  }
  .company { position: absolute; left: 160px; top: 340px; color: var(--white); }
  .company__name { display: flex; align-items: center; gap: 6px; font-size: 20px; font-weight: 800; line-height: 1; }
  .company__square { width: 20px; height: 20px; background: var(--white); }
  .company__sub { font-size: 8.5px; font-weight: 600; margin-top: 4px; margin-left: 26px; letter-spacing: 0.3px; }
  .contact { position: absolute; left: 38px; top: 418px; color: var(--white); font-weight: 800; font-size: 27px; line-height: 1; }
  .contact__row { display: flex; align-items: center; gap: 8px; margin-bottom: 12px; }
  .contact__icon { width: 20px; height: 20px; }
</style>
</head>
<body>
  <main class="billboard">
    <div class="pattern-area" role="img" aria-label="Soft orange and grey decorative line pattern"></div>

    <svg class="billboard__shapes" viewBox="0 0 760 534" aria-hidden="true">
      <polygon points="0,246 560,272 560,294 0,262" fill="var(--grey-band)"/>
      <polygon points="0,258 560,287 500,534 0,534" fill="var(--orange)"/>
    </svg>

    <div class="model-photo" role="img" aria-label="Photo of a delighted young woman in a denim jacket, hands on her chest"></div>

    <h1 class="headline">
      <div class="headline__lead">Make money</div>
      <div class="headline__main">By renting out</div>
      <div class="headline__sub">Your property</div>
      <div class="headline__sub headline__sub--indent">In the holidays</div>
    </h1>
    <div class="headline__mark">?</div>

    <div class="campaign">Boost<br>Your<br>Bookings</div>
    <div class="campaign__with">WITH</div>
    <div class="company">
      <div class="company__name"><span class="company__square"></span>HARBOURLINE</div>
      <div class="company__sub">PROPERTY MANAGEMENT</div>
    </div>

    <div class="contact">
      <div class="contact__row">
        <svg class="contact__icon" viewBox="0 0 24 24" aria-hidden="true"><path fill="#fff" d="M6.6 10.8a15.1 15.1 0 0 0 6.6 6.6l2.2-2.2a1 1 0 0 1 1-.25 11.4 11.4 0 0 0 3.6.57 1 1 0 0 1 1 1V20a1 1 0 0 1-1 1A17 17 0 0 1 3 4a1 1 0 0 1 1-1h3.5a1 1 0 0 1 1 1c0 1.25.2 2.45.57 3.57a1 1 0 0 1-.25 1z"/></svg>
        <span>+357 99 482 017</span>
      </div>
      <div class="contact__row">
        <svg class="contact__icon" viewBox="0 0 24 24" aria-hidden="true"><g fill="none" stroke="#fff" stroke-width="2"><circle cx="12" cy="12" r="9"/><ellipse cx="12" cy="12" rx="4" ry="9"/><path d="M3 12h18"/></g></svg>
        <span>HARBOURLINE.CY</span>
      </div>
    </div>
  </main>
</body>
</html>
```